Website for harborlyn mobile detailing.

Need a homepage, pages for: car and truck detailing, boat detailing, airplane detailing, about us, contact us. I have the domain name through quillnest so I will need the design uploaded on my domain. Also hoping to link other domains to this page.I would like to see the logo more pronounced. I would like to see a large phone number link to call my business. The layout looks nice but the pics need to depict car washing and waxing not car mechanics. i would like the colors of the webpage to incorporate the colors found in the logo in some way. I would like links to social media pages
Updates

Need extra days to review

Target Market(s)

Local customers in Vero Beach, Florida.

Number of Pages Required

5+ page

Colors

Designer to choose colors to be used in the design.

Requirements
Must have
• Easy to navigate, attractive pages with pictures and logo, professional looking. must have my phone number and logo very prevalent and links to call or go to home page. I would like links to my social media accounts on the home page.
Nice to have
• Easy to navigate, attractive pages with pictures and logo, professional looking.

```html
<!DOCTYPE html>
<html lang="en">
<head>
<meta charset="utf-8">
<title>Harborlyn Mobile Detailing</title>
<link href="https://fonts.googleapis.com/css2?family=Lato:wght@400;700;900&family=Roboto:wght@400;500&family=Titillium+Web:wght@600;700&display=swap" rel="stylesheet">
<style>
:root{
  --sky:#7bbfeb;
  --sky-card:#74b9e8;
  --footer:#53a2d6;
  --hero-dark:#2b3f6e;
  --brand-blue:#2a4f9e;
  --accent:#e8522e;
  --grey-bg:#f2f2f2;
  --grey-box:#e8e8e8;
  --ink:#333333;
  --white:#ffffff;
  --muted:#9a9a9a;
}
*{box-sizing:border-box;margin:0;padding:0}
html,body{width:1200px;height:2699px;overflow:hidden}
body{position:relative;background:var(--white);font-family:"Lato",sans-serif;color:var(--ink)}
.abs{position:absolute}

.topbar{left:0;top:0;width:1200px;height:46px;background:var(--sky);color:var(--white);font-size:13px;display:flex;justify-content:center;align-items:center;gap:18px}
.topbar span{display:flex;align-items:center;gap:5px}
.topbar .top-phone{font-weight:900;font-size:16px;letter-spacing:.5px}

.brand{left:0;top:46px;width:1200px;height:138px;display:flex;justify-content:center;align-items:center;gap:14px}
.brand-mark{width:50px;height:50px;border-radius:50%;background:var(--accent)}
.brand-name{font-family:"Titillium Web",sans-serif;font-weight:700;font-size:44px;line-height:1;color:var(--brand-blue)}

.nav{left:6px;top:184px;width:1188px;height:59px;background:var(--sky);display:flex;justify-content:center;align-items:center;gap:42px;font-family:"Titillium Web",sans-serif;font-weight:700;font-size:16px;color:var(--white)}
.nav .current{color:var(--accent);font-weight:600}

.hero{left:6px;top:243px;width:1188px;height:430px;background:linear-gradient(160deg,#4d6493 0%,var(--hero-dark) 55%,#22335c 100%);color:var(--white);text-align:center}
.hero-title{position:absolute;left:0;width:100%;top:160px;font-family:"Roboto",sans-serif;font-weight:500;font-size:37px;letter-spacing:7px}
.hero-sub{position:absolute;left:0;width:100%;top:210px;font-family:"Roboto",sans-serif;font-size:20px;letter-spacing:1px;color:#d8e0ee}
.hero-btns{position:absolute;left:0;width:100%;top:252px;display:flex;justify-content:center;gap:32px}
.btn{width:102px;height:40px;border-radius:20px;font-size:13px;font-weight:700;display:flex;align-items:center;justify-content:center}
.btn-solid{background:var(--accent)}
.btn-ghost{border:2px solid var(--accent);color:var(--accent)}
.hero-arrow{position:absolute;top:218px}
.call-now{position:absolute;right:18px;top:356px;height:52px;border-radius:26px;background:#3a3a3a;display:flex;align-items:center;gap:12px;padding:0 22px 0 5px;font-size:12px;text-align:left}
.call-now i{width:42px;height:42px;border-radius:50%;background:var(--accent);display:flex;align-items:center;justify-content:center}
.call-now small{display:block;font-size:11px;letter-spacing:1px;color:#cfcfcf}
.call-now strong{display:block;font-size:20px;font-weight:900;line-height:1.1}

.band{left:0;top:713px;width:1200px;height:1310px;background:var(--grey-bg)}
.band-gap{left:0;top:1346px;width:1200px;height:6px;background:var(--white)}

.card{top:758px;width:375px;height:543px;background:var(--sky-card);color:var(--white)}
.card-photo{height:214px}
.card-title{height:90px;border-bottom:1px solid rgba(255,255,255,.6);padding:34px 0 0 40px;font-family:"Titillium Web",sans-serif;font-weight:600;font-size:20px;color:#233a57}
.card-text{padding:38px 40px 0 40px;font-size:15.5px;line-height:27px}
.card-more{padding:28px 0 0 40px;font-weight:700;font-size:16px}

.reviews{left:122px;top:1359px;width:948px;height:414px;background:linear-gradient(180deg,#bdbdbd,#9c9c9c 60%,#8a8a8a);color:var(--white);text-align:center}
.reviews h2{padding-top:24px;font-family:"Titillium Web",sans-serif;font-weight:700;font-size:20px}
.reviews .rule{position:absolute;left:0;width:948px;top:76px;height:1px;background:rgba(255,255,255,.5)}
.stars{position:absolute;top:112px;left:0;width:100%;color:#f2c230;font-size:14px;letter-spacing:2px}
.quote{position:absolute;top:168px;left:60px;width:828px;font-size:13.5px;line-height:22px}
.review-title{position:absolute;top:240px;left:0;width:100%;font-weight:700;font-size:14px}
.review-name{position:absolute;top:270px;left:0;width:100%;font-size:13px}
.review-rule{position:absolute;left:34px;width:880px;top:298px;height:1px;background:rgba(255,255,255,.55)}
.dots{position:absolute;top:318px;left:0;width:100%;display:flex;justify-content:center;gap:6px}
.dots i{width:7px;height:7px;border-radius:50%;background:rgba(255,255,255,.6)}
.dots i:first-child{background:#7bbfeb}
.rev-arrow{position:absolute;top:192px;width:24px;height:24px;border:1px solid rgba(255,255,255,.6);border-radius:50%}

.about{left:148px;top:1809px;width:945px;height:202px;background:var(--grey-box);padding:28px 34px}
.about h3{font-family:"Titillium Web",sans-serif;font-weight:600;font-size:15px;margin-bottom:50px}
.about p{font-size:12.5px;line-height:23px}

.footer{left:6px;top:2048px;width:1188px;height:544px;background:var(--footer);color:var(--white)}
.fcol{position:absolute;top:40px}
.fcol h4{font-family:"Titillium Web",sans-serif;font-weight:600;font-size:15px;color:#1f3a55;padding-bottom:22px;border-bottom:1px solid rgba(255,255,255,.6)}
.fcol p{margin-top:22px;font-size:15.5px;line-height:27px}
.follow{margin-top:36px}
.socials{display:flex;gap:14px;margin-top:22px;padding-left:8px}
.socials i{width:34px;height:34px;background:#eeeeee;border-radius:3px;display:flex;align-items:center;justify-content:center}
.socials b{width:14px;height:14px;background:#7a7a7a;border-radius:2px}
.links a{display:block;color:var(--white);text-decoration:none;font-size:15.5px;padding:22px 0 12px;border-bottom:1px solid rgba(255,255,255,.35)}
.form label{display:block;font-weight:700;font-size:15px;color:#1f3a55;margin-top:24px}
.form label em{color:var(--accent);font-style:normal}
.field{background:var(--white);height:38px;border:1px solid #ccc}
.pair{display:flex;gap:14px;margin-top:6px}
.pair div{width:100px}
.pair small{display:block;font-size:12px;color:#1f3a55;margin-top:4px}
.send{margin-top:16px;width:68px;height:40px;background:#eeeeee;color:#555;font-size:15px;display:flex;align-items:center;justify-content:center;border:1px solid #ccc}

.copyright{left:0;top:2636px;width:1200px;text-align:center;font-size:12.5px;letter-spacing:1px;color:var(--muted)}
</style>
</head>
<body>

<div class="abs topbar">
  <span><svg width="12" height="12" viewBox="0 0 12 12"><path d="M1 2l3-1 4 1 3-1v9l-3 1-4-1-3 1z" fill="#fff"/></svg>Kestrel Yard</span>
  <span><svg width="10" height="13" viewBox="0 0 10 13"><path d="M5 0a4.5 4.5 0 0 1 4.5 4.5C9.5 8 5 13 5 13S.5 8 .5 4.5A4.5 4.5 0 0 1 5 0z" fill="#fff"/><circle cx="5" cy="4.5" r="1.7" fill="#7bbfeb"/></svg>Marlow Bay</span>
  <span class="top-phone"><svg width="14" height="14" viewBox="0 0 12 12"><path d="M2 1l2 0 1 3-1.3 1a7 7 0 0 0 3.3 3.3L8 7l3 1v2a1 1 0 0 1-1 1A9 9 0 0 1 1 2a1 1 0 0 1 1-1z" fill="#fff"/></svg>0100 555 0142</span>
</div>

<div class="abs brand">
  <span class="brand-mark"></span>
  <span class="brand-name">Harborlyn Mobile Detailing</span>
</div>

<nav class="abs nav">
  <span class="current">Home</span>
  <span>About Us</span>
  <span>Plane Detailing</span>
  <span>Truck Detailing</span>
  <span>Contact Us</span>
</nav>

<section class="abs hero" role="img" aria-label="Photo of a white motor boat in a hangar under a blue tint">
  <svg class="hero-arrow" style="left:14px" width="14" height="24" viewBox="0 0 14 24"><path d="M12 2L2 12l10 10" stroke="#fff" stroke-width="2" fill="none"/></svg>
  <svg class="hero-arrow" style="right:14px" width="14" height="24" viewBox="0 0 14 24"><path d="M2 2l10 10L2 22" stroke="#fff" stroke-width="2" fill="none"/></svg>
  <h1 class="hero-title">Harborlyn mobile detailing</h1>
  <p class="hero-sub">Profesional Services</p>
  <div class="hero-btns">
    <span class="btn btn-solid">Portfolio</span>
    <span class="btn btn-ghost">Prices</span>
  </div>
  <div class="call-now">
    <i><svg width="20" height="20" viewBox="0 0 12 12"><path d="M2 1l2 0 1 3-1.3 1a7 7 0 0 0 3.3 3.3L8 7l3 1v2a1 1 0 0 1-1 1A9 9 0 0 1 1 2a1 1 0 0 1 1-1z" fill="#fff"/></svg></i>
    <span><small>CALL NOW</small><strong>0100 555 0142</strong></span>
  </div>
</section>

<div class="abs band"></div>
<div class="abs band-gap"></div>

<article class="abs card" style="left:6px">
  <div class="card-photo" role="img" aria-label="Photo of a white boat on display" style="background:linear-gradient(135deg,#e8ecf0,#7d8894 60%,#2e3640)"></div>
  <h3 class="card-title">Boat Detailing</h3>
  <p class="card-text">Make your boat to stand out Lorem ipsum dolor sit amet, consectetur adipiscing elit. Vivamus interdum molestie sem, et egestas nisl …</p>
  <p class="card-more">Read More</p>
</article>
<article class="abs card" style="left:412px">
  <div class="card-photo" role="img" aria-label="Photo of a row of truck wheels" style="background:linear-gradient(135deg,#6c6f70,#2a2c2d 55%,#8b8f8c)"></div>
  <h3 class="card-title">Truck Detailing</h3>
  <p class="card-text">We make it perfect for you Lorem ipsum dolor sit amet, consectetur adipiscing elit. Vivamus interdum molestie sem, et egestas nisl consectetur sed. …</p>
  <p class="card-more">Read More</p>
</article>
<article class="abs card" style="left:821px">
  <div class="card-photo" role="img" aria-label="Photo of a small plane on an airfield at dusk" style="background:linear-gradient(180deg,#3a2a22,#6b4a32 50%,#4a4540)"></div>
  <h3 class="card-title">Plane Detailing</h3>
  <p class="card-text">A special flight Lorem ipsum dolor sit amet, consectetur adipiscing elit. Vivamus interdum molestie sem, et egestas nisl consectetur sed. …</p>
  <p class="card-more">Read More</p>
</article>

<section class="abs reviews" role="img" aria-label="Background photo of a smiling customer">
  <h2>Customers’ Opinion</h2>
  <div class="rule"></div>
  <div class="stars">★★★★★</div>
  <span class="rev-arrow" style="left:42px"></span>
  <span class="rev-arrow" style="right:42px"></span>
  <p class="quote">“The whole removal process was carried out extremely well.Time keeping and packing all good. Communication was quick, responsive and friendly from Dorian and the team were very helpful in all respects.”</p>
  <p class="review-title">Great Service</p>
  <p class="review-name">Ms R Talbot</p>
  <div class="review-rule"></div>
  <div class="dots"><i></i><i></i></div>
</section>

<section class="abs about">
  <h3>About Us</h3>
  <p>Our main business is detailing cars, boats, and airplanes. Wash, wax, degrease, we do it all. I would like a separate page for cars, boats, and airplanes. My business is located in Coral Point Florida in Palmetto County. I would like to emphasize that I have been in coral for over 30 years and that this business is locally owned and operated. Customer service and satisfaction is our main goal.</p>
</section>

<footer class="abs footer">
  <div class="fcol" style="left:17px;width:350px">
    <h4>About Us</h4>
    <p>Lorem ipsum dolor sit amet, consectetur adipiscing elit. Ut ac sapien ac mauris sollicitudin imperdiet mattis id mauris. Nam eu fringilla ipsum. Suspendisse congue ac ligula vel bibendum. Pellentesque ligula lacus, placerat id convallis at, condimentum ut odio. Donec varius nulla ac justo accumsan malesuada non gravida nulla.</p>
    <h4 class="follow">Follow Us</h4>
    <div class="socials">
      <i><svg width="16" height="12" viewBox="0 0 16 12"><rect x="1" y="1" width="14" height="10" fill="none" stroke="#777" stroke-width="1.5"/><path d="M1 1l7 6 7-6" fill="none" stroke="#777" stroke-width="1.5"/></svg></i>
      <i><b></b></i><i><b></b></i><i><b></b></i>
    </div>
  </div>
  <div class="fcol links" style="left:422px;width:350px">
    <h4>Our Services</h4>
    <a>Boat Detailing</a>
    <a>Truck Detailing</a>
    <a>Plane Detailing</a>
    <a>About Us</a>
    <a style="border:none">Contact Us</a>
  </div>
  <div class="fcol form" style="left:828px;width:345px">
    <h4>Get in touch</h4>
    <label>Name <em>*</em></label>
    <div class="pair"><div><div class="field"></div><small>First</small></div><div><div class="field"></div><small>Last</small></div></div>
    <label>Email <em>*</em></label>
    <div class="field" style="width:206px;margin-top:6px"></div>
    <label>Comment or Message <em>*</em></label>
    <div class="field" style="height:122px;margin-top:6px"></div>
    <div class="send">Send</div>
  </div>
</footer>

<p class="abs copyright">COPYRIGHT © 2018 · SUMMIT PRO THEME ON KEYSTONE FRAMEWORK · PRESSKIT · LOG OUT</p>

</body>
</html>
```